Greeting Cards - Order on line, choose from thousands - mailed for you

We need a Friendline design for an online company that deals with greeting cards and gifts. Order online and the company prints, puts in envelopes, stamps and mails. I am an independent distributor for Post Ahead Notes see www.postaheadnotes-example.com or mailvoro.com it is a direct marketing company and I can't use any of their trademarked material on my page. My company name is Brightwhisk Greetings. This is a product (?) service that helps people connect with relatives, friends, customers, or clients with beautiful cards that are mailed not emailed. In addition they have a wide variety of gifts that can be selected and mailed along with the card if the customer chooses. Please visit the URLs above to get an idea of what this entails.

```html
<!DOCTYPE html>
<html lang="en">
<head>
<meta charset="utf-8">
<title>Brightwhisk Greetings – Cover Page</title>
<link rel="stylesheet" href="https://fonts.googleapis.com/css2?family=Nunito:wght@900&family=Roboto:wght@400;700&display=swap">
<style>
  :root {
    --page-bg: #e9ebee;
    --bar-blue: #3b5998;
    --bar-text: #ffffff;
    --bar-muted: #9cb4d8;
    --input-border: #1d2a5b;
    --button-bg: #5b74a8;
    --button-border: #29447e;
    --wood-dark: #2f2f2f;
    --wood-mid: #5c5c5c;
    --wood-light: #8a8a8a;
    --floor-light: #b0b0b0;
    --headline-fill: #000000;
    --headline-edge: #ffffff;
    --gift-blue: #5b8fd6;
    --gift-green: #8fd12a;
    --bloom-pink: #c99ab8;
    --gift-red: #d9432c;
    --logo-bg: #ffffff;
    --logo-border: #c9c9c9;
    --logo-ink: #333333;
    --tab-bg: #ffffff;
    --tab-text: #4b4f56;
    --tab-active: #1d2129;
    --tab-line: #e5e5e5;
  }
  html, body {
    margin: 0;
    padding: 0;
    width: 1200px;
    height: 606px;
    overflow: hidden;
    background: var(--page-bg);
  }
  .canvas {
    position: relative;
    width: 1200px;
    height: 606px;
    overflow: hidden;
    font-family: "Roboto", Arial, sans-serif;
  }

  /* Top bar */
  .top-bar {
    position: absolute;
    left: 0; top: 0;
    width: 1200px; height: 99px;
    background: var(--bar-blue);
  }
  .top-bar__name {
    position: absolute;
    left: 6px; top: 22px;
    margin: 0;
    font-family: "Roboto", Arial, sans-serif;
    font-weight: 700;
    font-size: 46px;
    line-height: 56px;
    color: var(--bar-text);
  }
  .login-field {
    position: absolute;
    top: 4px;
    width: 211px;
  }
  .login-field--email { left: 660px; }
  .login-field--password { left: 891px; }
  .login-field__label {
    display: block;
    font-size: 14px;
    line-height: 17px;
    color: var(--bar-text);
  }
  .login-field__input {
    display: block;
    margin-top: 4px;
    width: 205px;
    height: 27px;
    background: #ffffff;
    border: 1px solid var(--input-border);
  }
  .login-field__note {
    display: flex;
    align-items: center;
    gap: 6px;
    margin-top: 8px;
    font-size: 13px;
    color: var(--bar-muted);
  }
  .login-field__check {
    width: 12px; height: 12px;
    background: #f4f4f4;
    border: 1px solid #8b9dc3;
  }
  .login-button {
    position: absolute;
    left: 1122px; top: 27px;
    width: 69px; height: 29px;
    background: var(--button-bg);
    border: 1px solid var(--button-border);
    color: var(--bar-text);
    font-weight: 700;
    font-size: 14px;
    line-height: 29px;
    text-align: center;
    box-sizing: border-box;
  }

  /* Cover */
  .cover {
    position: absolute;
    left: 0; top: 99px;
    width: 1200px; height: 441px;
    overflow: hidden;
    background: linear-gradient(180deg, var(--wood-dark) 0%, var(--wood-mid) 45%, var(--wood-light) 70%, var(--floor-light) 100%);
  }
  .headline {
    position: absolute;
    margin: 0;
    font-family: "Nunito", "Arial Rounded MT Bold", sans-serif;
    font-weight: 900;
    color: var(--headline-fill);
    white-space: nowrap;
    line-height: 1;
    text-shadow:
      2px 0 0 var(--headline-edge), -2px 0 0 var(--headline-edge),
      0 2px 0 var(--headline-edge), 0 -2px 0 var(--headline-edge),
      2px 2px 0 var(--headline-edge), -2px -2px 0 var(--headline-edge),
      2px -2px 0 var(--headline-edge), -2px 2px 0 var(--headline-edge);
  }
  .headline--lead { left: 25px; top: 24px; font-size: 41px; }
  .headline--second { left: 113px; top: 74px; font-size: 38px; }
  .headline--third { left: 113px; top: 122px; font-size: 38px; }
  .gift-scene {
    position: absolute;
    left: 543px; top: 56px;
    width: 627px; height: 385px;
    border-radius: 30px 30px 0 0;
    background:
      radial-gradient(ellipse at 82% 30%, var(--bloom-pink) 0%, rgba(201,154,184,0) 45%),
      radial-gradient(ellipse at 25% 40%, var(--gift-blue) 0%, rgba(91,143,214,0) 42%),
      radial-gradient(ellipse at 30% 18%, var(--gift-green) 0%, rgba(143,209,42,0) 25%),
      radial-gradient(ellipse at 62% 70%, var(--gift-red) 0%, rgba(217,67,44,0) 40%);
  }

  /* Tabs */
  .page-tabs {
    position: absolute;
    left: 258px; top: 540px;
    width: 942px; height: 66px;
    background: var(--tab-bg);
    display: flex;
    align-items: stretch;
  }
  .page-tabs__item {
    position: relative;
    padding: 0 24px;
    font-size: 18px;
    line-height: 66px;
    color: var(--tab-text);
    border-right: 1px solid var(--tab-line);
  }
  .page-tabs__item--active {
    color: var(--tab-active);
    font-weight: 700;
  }
  .page-tabs__item--active::after {
    content: "";
    position: absolute;
    left: 22px; right: 22px; bottom: 0;
    height: 4px;
    background: var(--bar-blue);
  }
  .page-tabs__item--more { border-right: none; }
  .page-tabs__caret { font-size: 11px; margin-left: 4px; }

  /* Profile square */
  .profile-logo {
    position: absolute;
    left: 20px; top: 348px;
    width: 231px; height: 231px;
    background: var(--logo-bg);
    border: 3px solid var(--logo-border);
    display: flex;
    align-items: center;
    justify-content: center;
    overflow: hidden;
  }
  .profile-logo__text {
    font-family: "Roboto", Arial, sans-serif;
    font-weight: 400;
    font-size: 82px;
    letter-spacing: 4px;
    color: var(--logo-ink);
    transform: rotate(-45deg);
  }
</style>
</head>
<body>
  <main class="canvas">
    <header class="top-bar">
      <p class="top-bar__name">Friendline</p>
      <div class="login-field login-field--email">
        <span class="login-field__label">Email or Phone</span>
        <span class="login-field__input"></span>
        <span class="login-field__note"><span class="login-field__check"></span>Keep me logged in</span>
      </div>
      <div class="login-field login-field--password">
        <span class="login-field__label">Password</span>
        <span class="login-field__input"></span>
        <span class="login-field__note">Forgot your password?</span>
      </div>
      <div class="login-button">Log In</div>
    </header>

    <section class="cover">
      <h1 class="headline headline--lead">1000+ Cards and Gifts to choose</h1>
      <p class="headline headline--second">Comfort of ordering online</p>
      <p class="headline headline--third">We mail to your dear ones</p>
      <div class="gift-scene" role="img" aria-label="Wrapped gift boxes with ribbons, greeting cards and a vase of roses on a wooden floor"></div>
    </section>

    <nav class="page-tabs">
      <span class="page-tabs__item page-tabs__item--active">Timeline</span>
      <span class="page-tabs__item">About</span>
      <span class="page-tabs__item">Photos</span>
      <span class="page-tabs__item">Reviews</span>
      <span class="page-tabs__item page-tabs__item--more">More<span class="page-tabs__caret">▼</span></span>
    </nav>

    <div class="profile-logo">
      <span class="profile-logo__text">LOGO</span>
    </div>
  </main>
</body>
</html>
```